Author/ Speaker Business Card design

I need a business card designed that will go with the branding that is already on my book and website. I like clean and straightforward, but I am not opposed to something more 'innovative'.

Target Market(s)

Colleges and Universities, educational institutions

Industry/Entity Type

Education

Contact Information for Business Card

Standard size. It should be able to be printed on good quality white or ivory paper.

Font styles to use
Sans Serif

Colors
0355a3

Requirements
Must have
• There's a blue on my website. It should have some blue. My logo is at the top. It should have the logo incorporated somewhere on it. My name, Author | Speaker | Teacher | Trainer, my phone number (+31 64-207 5819), my email address (milo@theboldlearner.example), Social media icons (twitter, Instagram, LinkedIn) with the addresses (twitter @writermilofenwick, Instagram - theboldlearner, LinkedIn - theboldlearner) By they way, the website is www.theboldlearner.example. There is a photo of the book on the website. Also, my full name is Milo Fenwick
Nice to have
• Try to use the font that is on the website and book. Also, if you could get that blue, that would be great.
Should not have
• My photo

```html
<!DOCTYPE html>
<html lang="en">
<head>
<meta charset="utf-8">
<title>The Bold Learner — Business Card</title>
<link rel="stylesheet" href="https://fonts.googleapis.com/css2?family=Montserrat:wght@400;600&display=swap">
<style>
  :root{
    --brand-blue:#0355a3;
    --brand-blue-deep:#02488c;
    --card-white:#ffffff;
    --page-bg:#eceae6;
    --ink:#1f3550;
    --tint-light:#e6eef7;
    --tint-mid:#c4d6ea;
  }
  *{margin:0;padding:0;box-sizing:border-box}
  html,body{width:771px;height:1200px;overflow:hidden;background:var(--page-bg)}
  body{font-family:"Montserrat",Arial,sans-serif;position:relative}
  .card{
    position:absolute;left:65px;width:640px;height:366px;
    background:var(--card-white);
    box-shadow:0 6px 18px rgba(0,0,0,.18);
    overflow:hidden;
  }
  .card--front{top:150px}
  .card--back{top:684px}
  .card svg.shapes{position:absolute;inset:0}
  .logo{
    position:absolute;color:var(--brand-blue);
    font-weight:600;font-size:30px;line-height:1.05;letter-spacing:-.5px;
    display:flex;align-items:center;gap:10px;
  }
  .logo__mark{width:16px;height:16px;background:var(--brand-blue);flex:none}
  .card--front .logo{left:48px;top:120px}
  .card--back .logo{left:40px;top:36px;font-size:24px}
  .name{
    text-transform:uppercase;letter-spacing:7px;font-weight:400;font-size:22px;white-space:nowrap;
  }
  .roles{font-size:10.5px;letter-spacing:.6px;text-transform:uppercase;margin-top:6px;white-space:nowrap}
  .front-id{position:absolute;left:268px;top:284px;color:#fff}
  .back-id{position:absolute;left:40px;top:170px;color:var(--brand-blue)}
  .back-id .roles{font-weight:600}
  .contacts{position:absolute;left:40px;top:250px;list-style:none;color:var(--ink);font-size:13px}
  .contacts li{display:flex;align-items:center;gap:10px;margin-bottom:10px}
  .contacts svg{width:14px;height:14px;flex:none}
  .website{position:absolute;left:40px;top:104px;color:var(--brand-blue);font-size:13px}
  .socials{position:absolute;left:414px;top:60px;list-style:none;color:#fff;font-size:12.5px}
  .socials li{display:flex;align-items:center;gap:9px;margin-bottom:46px;white-space:nowrap}
  .socials li:nth-child(2){margin-left:-10px}
  .socials li:nth-child(3){margin-left:-20px}
  .socials .dot{width:12px;height:12px;background:#fff;flex:none}
</style>
</head>
<body>

<section class="card card--front" aria-label="Card front">
  <svg class="shapes" width="640" height="366" viewBox="0 0 640 366">
    <defs>
      <linearGradient id="bookTone" x1="0" y1="0" x2="1" y2="1">
        <stop offset="0" stop-color="var(--tint-light)"/>
        <stop offset="1" stop-color="var(--tint-mid)"/>
      </linearGradient>
    </defs>
    <path role="img" aria-label="Book cover image area" d="M400 0 H640 V200 C590 215 520 235 470 250 C440 200 410 90 400 0 Z" fill="url(#bookTone)"/>
    <path d="M595 0 H640 V42 Z" fill="var(--brand-blue)"/>
    <path d="M170 366 L640 366 L640 200 C590 215 520 235 470 250 L250 250 Z" fill="var(--brand-blue)"/>
  </svg>
  <div class="logo"><span class="logo__mark"></span><span>The Bold<br>Learner</span></div>
  <div class="front-id">
    <p class="name">Milo Fenwick</p>
    <p class="roles">Author | Speaker | Teacher | Trainer</p>
  </div>
</section>

<section class="card card--back" aria-label="Card back">
  <svg class="shapes" width="640" height="366" viewBox="0 0 640 366">
    <defs>
      <linearGradient id="bookToneBack" x1="0" y1="0" x2="1" y2="1">
        <stop offset="0" stop-color="var(--tint-light)"/>
        <stop offset="1" stop-color="var(--tint-mid)"/>
      </linearGradient>
    </defs>
    <path role="img" aria-label="Book cover image area" d="M565 150 H640 V366 H530 Z" fill="url(#bookToneBack)"/>
    <path d="M400 0 H590 L530 366 H340 Z" fill="var(--brand-blue)"/>
    <path d="M530 366 L555 300 L578 366 Z" fill="var(--brand-blue-deep)"/>
  </svg>
  <div class="logo"><span class="logo__mark"></span><span>The Bold<br>Learner</span></div>
  <p class="website">www.theboldlearner.example</p>
  <div class="back-id">
    <p class="name">Milo Fenwick</p>
    <p class="roles">Author | Speaker | Teacher | Trainer</p>
  </div>
  <ul class="contacts">
    <li>
      <svg viewBox="0 0 24 24" aria-hidden="true"><path fill="var(--brand-blue)" d="M6.6 10.8a15 15 0 0 0 6.6 6.6l2.2-2.2a1 1 0 0 1 1-.25 11.4 11.4 0 0 0 3.6.57 1 1 0 0 1 1 1V20a1 1 0 0 1-1 1A17 17 0 0 1 3 4a1 1 0 0 1 1-1h3.5a1 1 0 0 1 1 1c0 1.25.2 2.450.57 3.57a1 1 0 0 1-.25 1Z"/></svg>
      <span>+31 64-207 5819</span>
    </li>
    <li>
      <svg viewBox="0 0 24 24" aria-hidden="true"><path fill="var(--brand-blue)" d="M3 5h18v14H3Z"/><path fill="none" stroke="#fff" stroke-width="1.6" d="M3.5 6 12 13l8.5-7"/></svg>
      <span>milo@theboldlearner.example</span>
    </li>
  </ul>
  <ul class="socials">
    <li><span class="dot"></span><span>theboldlearner</span></li>
    <li><span class="dot"></span><span>theboldlearner</span></li>
    <li><span class="dot"></span><span>@writermilofenwick</span></li>
  </ul>
</section>

</body>
</html>
```